L.M.T. Penrow

I am an indie author and already have a Facebook page. However, I would like it to be more professional and look less like a private Facebook page.

```html
<!DOCTYPE html>
<html lang="en">
<head>
<meta charset="utf-8">
<title>Strata – L.M.T. Penrow</title>
<link rel="stylesheet" href="https://fonts.googleapis.com/css2?family=Kaushan+Script&family=Oswald:wght@400;600&family=Cabin:ital,wght@0,400;1,400&display=swap">
<style>
  :root {
    --bg: #050608;
    --gold: #f1c43a;
    --gold-light: #fff2a8;
    --gold-dark: #c8901a;
    --white: #ffffff;
    --ghost: rgba(120, 125, 135, 0.14);
    --door-blue: #2f8fe6;
    --door-glow: rgba(60, 150, 240, 0.55);
    --star: #f3c531;
    --badge: #c9302c;
  }
  html, body {
    margin: 0;
    padding: 0;
    overflow: hidden;
    background: var(--bg);
  }
  .banner {
    position: relative;
    width: 1200px;
    height: 464px;
    overflow: hidden;
    background:
      radial-gradient(ellipse 520px 110px at 900px 470px, rgba(40, 90, 150, 0.28), transparent 70%),
      linear-gradient(180deg, #030405 0%, #07090c 70%, #0b1420 100%);
    font-family: "Cabin", sans-serif;
  }
  .door-light {
    position: absolute;
    right: 0;
    top: 30px;
    width: 130px;
    height: 440px;
    background: linear-gradient(90deg, transparent 0%, rgba(30, 100, 190, 0.25) 35%, var(--door-blue) 70%, #7cc3ff 100%);
    filter: blur(6px);
  }
  .door-spill {
    position: absolute;
    right: 0;
    bottom: -20px;
    width: 420px;
    height: 120px;
    background: radial-gradient(ellipse at 100% 60%, var(--door-glow), transparent 70%);
  }
  .book {
    position: absolute;
    left: 24px;
    top: 28px;
    width: 320px;
    height: 414px;
  }
  .tagline {
    position: absolute;
    left: 392px;
    top: 26px;
    width: 600px;
    margin: 0;
    line-height: 1;
    text-align: center;
    font-size: 25px;
    color: var(--gold);
    letter-spacing: 0.3px;
  }
  .title-ghost {
    position: absolute;
    left: 400px;
    top: 150px;
    margin: 0;
    font-family: "Kaushan Script", cursive;
    font-size: 220px;
    line-height: 1;
    color: var(--ghost);
    transform: rotate(-4deg);
  }
  .title {
    position: absolute;
    left: 420px;
    top: 50px;
    margin: 0;
    font-family: "Kaushan Script", cursive;
    font-size: 190px;
    font-weight: 400;
    line-height: 1;
    background: linear-gradient(180deg, var(--gold-light) 0%, var(--gold) 45%, var(--gold-dark) 100%);
    -webkit-background-clip: text;
    background-clip: text;
    color: transparent;
    transform: rotate(-4deg);
  }
  .author {
    position: absolute;
    right: 200px;
    top: 244px;
    margin: 0;
    line-height: 1;
    font-family: "Oswald", sans-serif;
    font-weight: 600;
    font-size: 58px;
    color: var(--white);
    letter-spacing: 1px;
  }
  .website {
    position: absolute;
    right: 206px;
    top: 306px;
    margin: 0;
    line-height: 1;
    font-family: "Oswald", sans-serif;
    font-size: 21px;
    color: var(--gold);
  }
  .review {
    position: absolute;
    left: 427px;
    top: 362px;
    display: flex;
    align-items: center;
    gap: 18px;
  }
  .stars { display: block; }
  .quote {
    margin: 0;
    line-height: 1;
    font-size: 25px;
    color: var(--white);
  }
  .source {
    position: absolute;
    left: 665px;
    top: 402px;
    display: flex;
    align-items: center;
    gap: 10px;
  }
  .source-badge {
    width: 34px;
    height: 34px;
    background: var(--badge);
    border-radius: 3px;
  }
  .source-name {
    font-size: 17px;
    font-style: italic;
    color: var(--white);
  }
</style>
</head>
<body>
<main class="banner">
  <div class="door-light"></div>
  <div class="door-spill"></div>

  <svg class="book" viewBox="0 0 320 414" role="img" aria-label="Book cover of Strata: a young woman's face above a burst of fire and a silhouetted figure">
    <defs>
      <linearGradient id="cover" x1="0" y1="0" x2="0" y2="1">
        <stop offset="0" stop-color="#3a2a30"/>
        <stop offset="0.35" stop-color="#8a5a4a"/>
        <stop offset="0.55" stop-color="#e07a2a"/>
        <stop offset="0.75" stop-color="#5a3a6a"/>
        <stop offset="1" stop-color="#1c1a2a"/>
      </linearGradient>
      <linearGradient id="spine" x1="0" y1="0" x2="0" y2="1">
        <stop offset="0" stop-color="#1e1618"/>
        <stop offset="0.55" stop-color="#6a3a24"/>
        <stop offset="1" stop-color="#111018"/>
      </linearGradient>
    </defs>
    <polygon points="0,14 46,0 46,414 0,402" fill="url(#spine)"/>
    <polygon points="46,0 316,8 316,406 46,414" fill="url(#cover)"/>
    <polygon points="46,0 56,1 56,413 46,414" fill="rgba(255,255,255,0.12)"/>
  </svg>

  <p class="tagline">Opening his door to Selene was a grave mistake</p>

  <p class="title-ghost" aria-hidden="true">Strata</p>
  <h1 class="title">Strata</h1>

  <h2 class="author">L.M.T. Penrow</h2>
  <p class="website">http://www.lmt-penrow.com/</p>

  <div class="review">
    <svg class="stars" width="96" height="17" viewBox="0 0 104 18" aria-label="Five stars">
      <g fill="var(--star)">
        <polygon points="9,0 11.6,6 18,6.6 13.2,10.8 14.6,17 9,13.8 3.4,17 4.8,10.8 0,6.6 6.4,6"/>
        <polygon transform="translate(21.5 0)" points="9,0 11.6,6 18,6.6 13.2,10.8 14.6,17 9,13.8 3.4,17 4.8,10.8 0,6.6 6.4,6"/>
        <polygon transform="translate(43 0)" points="9,0 11.6,6 18,6.6 13.2,10.8 14.6,17 9,13.8 3.4,17 4.8,10.8 0,6.6 6.4,6"/>
        <polygon transform="translate(64.5 0)" points="9,0 11.6,6 18,6.6 13.2,10.8 14.6,17 9,13.8 3.4,17 4.8,10.8 0,6.6 6.4,6"/>
        <polygon transform="translate(86 0)" points="9,0 11.6,6 18,6.6 13.2,10.8 14.6,17 9,13.8 3.4,17 4.8,10.8 0,6.6 6.4,6"/>
      </g>
    </svg>
    <p class="quote">“Riveting thriller that keeps you on edge...”</p>
  </div>

  <div class="source">
    <div class="source-badge"></div>
    <span class="source-name">Indie Press Digest</span>
  </div>
</main>
</body>
</html>
```